New Wordpress Website for TV Production Company Needed

I need to redo my website lanternfold.example

I am looking for a fresh look and style using the same color scheme of red and white as the current website.
Updates

I am extending the deadline so I can get more designs submitted. So far the majority of the submissions have the same look and feel. Except for 1 so far.

Industry/Entity Type

TV Production

Coding

Coded - Design and coding required

Number of Pages Required

1 page

Requirements
Must have
• MUST be in WordPress. The project MUST have all of the sections that I currently have in my current website, including a video presentation so my clients can see our work. MUST also use my existing logo. No new logo designs.
Nice to have
• Nice to have an interesting new way to present the video. I LOVE how this site works. https://vardo.plimwave.example/. would be great to have something like this, I love how interactive and how the posters/images are large

```html
<!DOCTYPE html>
<html lang="en">
<head>
<meta charset="utf-8">
<title>Lanternfold Post, Inc. — Post-Production</title>
<link href="https://fonts.googleapis.com/css2?family=Bebas+Neue&family=Montserrat:wght@400;500;600;700&display=swap" rel="stylesheet">
<style>
:root{
  --bg:#060609;
  --bg-2:#0d0d13;
  --card:#14141b;
  --red:#e8132a;
  --blue:#2b2fe0;
  --purple:#7a1ea8;
  --white:#ffffff;
  --muted:#c9c9d2;
  --field:#ffffff;
}
*{box-sizing:border-box;margin:0;padding:0}
html,body{width:1200px;height:4677px;overflow:hidden}
body{background:var(--bg);color:var(--white);font-family:"Montserrat",sans-serif;position:relative}
.abs{position:absolute}
.heading{font-family:"Bebas Neue",sans-serif;font-weight:400;letter-spacing:1px;font-size:46px;line-height:1}
.heading-center{left:0;width:1200px;text-align:center}
.rule{display:block;width:110px;height:4px;background:var(--red);margin:12px auto 0}
.rule-left{margin-left:0}

/* nav */
.site-nav{top:0;left:0;width:1200px;height:67px;background:#07070b;z-index:5}
.brand{left:143px;top:18px;font-size:24px;font-weight:700;color:var(--red)}
.brand small{display:block;font-size:10px;text-align:right;margin-top:-4px}
.menu{left:484px;top:26px;display:flex;gap:0;list-style:none;font-size:14px;font-weight:600}
.menu li{width:100px}
.menu li:first-child{width:90px}
.menu .active{position:relative}
.menu .active::after{content:"";position:absolute;left:10px;top:22px;width:30px;height:2px;background:var(--red)}

/* hero */
.hero-photo{top:67px;left:0;width:1200px;height:600px;background:radial-gradient(ellipse at 78% 40%,#6a2a20 0%,#2a1216 30%,#0d1a22 60%,#060609 100%)}
.hero-title{left:143px;top:160px;font-size:68px;line-height:1.03}
.hero-dots{left:70px;top:266px;display:flex;flex-direction:column;gap:9px}
.hero-dots span{width:12px;height:12px;border:2px solid #fff;border-radius:50%}
.hero-dots .on{border-color:var(--red);background:radial-gradient(var(--red) 40%,transparent 45%)}
.btn{display:inline-flex;align-items:center;justify-content:center;font-weight:700;font-size:15px;color:#fff;background:var(--red);border:3px solid var(--blue);box-shadow:0 0 0 2px var(--red)}
.hero-btn{left:147px;top:345px;width:154px;height:42px}

/* about */
.about-shot{left:143px;top:708px;width:410px;height:336px;background:linear-gradient(135deg,#3a4048,#8b8f86 40%,#1c2228 70%,#2e3a2e)}
.about-desk{left:288px;top:988px;width:312px;height:228px;background:linear-gradient(135deg,#2a2f38,#0e1014 60%,#2a1a40);border:3px solid var(--red);box-shadow:3px 3px 0 var(--blue)}
.about-text{left:664px;top:735px;width:396px;text-align:center}
.about-text h2{margin-bottom:10px}
.about-text .lead{font-size:15px;line-height:1.6;margin-top:40px}
.about-text .sub{font-size:12.5px;line-height:1.9;margin-top:14px}
.about-btn{left:795px;top:1137px;width:132px;height:42px;font-size:14px}

/* services */
.services-head{top:1302px}
.services-intro{left:140px;top:1398px;width:920px;text-align:center;font-size:16.5px;font-weight:500;line-height:1.9}
.service{top:1507px;width:290px;height:330px;display:flex;flex-direction:column;justify-content:flex-end;align-items:center;padding-bottom:26px;text-align:center}
.service h3{font-size:16px;font-weight:600;letter-spacing:.5px}
.service p{font-size:13px;line-height:1.7;margin-top:10px;width:220px}
.svc-1{left:0;background:linear-gradient(160deg,#2d3a2e,#15181c 55%,#3b1a5a)}
.svc-2{left:304px;background:linear-gradient(180deg,#5a1c26,#a01b2a 70%,#c9202e);padding-bottom:30px}
.svc-3{left:608px;background:linear-gradient(160deg,#3a3f44,#16181b 70%)}
.svc-4{left:911px;background:radial-gradient(circle at 50% 45%,#2f6a90 0%,#7d8b94 25%,#d9c6bc 55%,#8f7468 100%);width:289px}
.svc-icon{margin-bottom:18px}
.arrow-btn{width:36px;height:36px;border-radius:50%;background:#fff;display:flex;align-items:center;justify-content:center}
.svc-prev{left:15px;top:1654px}
.svc-next{left:1148px;top:1654px}

/* videos */
.videos-head{top:1935px}
.video-side{top:2085px;width:140px;height:288px;background:linear-gradient(160deg,#2a2d33,#14161a);border-radius:10px;opacity:.7}
.video-left{left:143px}
.video-right{left:915px}
.video-main{left:276px;top:2047px;width:648px;height:362px;border:2px solid #fff;border-radius:16px;overflow:hidden;background:radial-gradient(ellipse at 40% 45%,#6a2f1c,#2a1a14 40%,#101418 75%)}
.play{left:278px;top:126px;width:90px;height:90px;border-radius:50%;border:4px solid #fff;background:rgba(0,0,0,.35);display:flex;align-items:center;justify-content:center}
.click-play{left:384px;top:210px;font-size:31px;font-weight:700}
.player-bar{left:18px;bottom:10px;width:610px;height:30px;display:flex;align-items:center;gap:10px}
.pb-btn{width:42px;height:30px;background:#111;border-radius:4px;display:flex;align-items:center;justify-content:center}
.pb-track{flex:1;height:30px;background:rgba(20,20,24,.85);border-radius:4px;position:relative}
.pb-time{position:absolute;left:-8px;top:-12px;font-size:9px;background:#111;padding:1px 4px;border-radius:2px}
.video-dots{left:570px;top:2441px;display:flex;gap:4px}
.video-dots span{width:10px;height:10px;border:1px solid #aaa;border-radius:50%}
.video-dots .on{background:var(--red);border-color:var(--red)}

/* projects */
.projects{top:2532px;left:0;width:1200px;height:663px;background:linear-gradient(180deg,#07070b 0%,#1a0508 60%,#2a060c 100%)}
.projects-head{left:143px;top:2615px}
.poster{top:2713px;width:284px;height:358px;border:3px solid #222}
.poster-1{left:147px;background:linear-gradient(180deg,#9fc0d8,#e6d2c2 50%,#8aa4b6)}
.poster-2{left:461px;width:278px;background:radial-gradient(ellipse at 50% 45%,#5a5a5a,#1a1a1a 60%,#050505)}
.poster-3{left:771px;width:278px;background:linear-gradient(180deg,#8a0f18,#c8202a 50%,#6a0a12)}
.poster-label{top:3101px;width:284px;text-align:center;font-size:16px;font-weight:600;letter-spacing:.5px}
.proj-arrow{top:2880px}

/* news */
.news-head{top:3298px}
.news-card{width:460px;height:170px;background:var(--card);display:flex;padding:8px 0 0 8px}
.news-card.dark{background:#1c1c25}
.news-logo{width:180px;height:84px;background:#fff;border:3px solid var(--red);box-shadow:2px 2px 0 var(--blue);display:flex;align-items:center;justify-content:center;color:#222;font-size:19px;font-weight:600;flex-shrink:0}
.news-logo.yellow{background:#f2c21b;color:#111}
.news-body{padding:6px 18px 0 26px}
.news-body h4{font-size:15px;font-weight:600;line-height:1.6}
.news-body p{font-size:12px;line-height:1.7;margin-top:8px;color:var(--muted)}
.news-body a{display:block;margin-top:8px;color:var(--red);font-size:13px;font-weight:600;text-decoration:none;letter-spacing:.5px}

/* clients */
.clients-head{top:3864px}
.client{top:3962px;width:172px;height:86px;background:#fff;display:flex;align-items:center;justify-content:center;color:#111;font-size:24px;font-weight:700}
.client.faded{background:#15151b;color:#4a4a55}

/* footer */
.foot-col h5{font-size:17px;font-weight:600;letter-spacing:.5px;margin-bottom:24px}
.quick{left:143px;top:4306px}
.quick ul{list-style:none;font-size:14px;line-height:2.05}
.contact{left:378px;top:4306px}
.contact li{list-style:none;display:flex;align-items:center;gap:14px;font-size:13.5px;margin-bottom:19px}
.c-ico{width:20px;height:20px;border-radius:50%;background:var(--blue);display:flex;align-items:center;justify-content:center}
.quote{left:788px;top:4306px;width:267px}
.field{display:block;width:267px;height:38px;background:var(--field);border-radius:3px;color:#999;font-size:11px;padding:12px 10px;margin-bottom:9px}
.field.msg{height:58px}
.submit{display:inline-flex;width:156px;height:38px;background:var(--red);align-items:center;justify-content:center;font-weight:700;font-size:15px;letter-spacing:.5px;margin-top:6px}
.copyright{left:0;top:4648px;width:1200px;text-align:center;font-size:12px;color:#d0d0d8}
</style>
</head>
<body>

<header class="site-nav abs">
  <div class="brand abs">Lanternfold<small>POST, INC.</small></div>
  <ul class="menu abs">
    <li class="active">HOME</li><li>ABOUT</li><li>SERVICES</li><li>CONTACT</li><li>CLIENTS</li><li>NEWS</li>
  </ul>
</header>

<section class="hero">
  <div class="hero-photo abs" role="img" aria-label="Colorist working at an editing desk with monitors in a dark studio"></div>
  <div class="hero-dots abs"><span></span><span class="on"></span><span></span></div>
  <h1 class="heading hero-title abs">WELCOME TO<br>LANTERNFOLD POST</h1>
  <span class="btn hero-btn abs">GET STARTED</span>
  <svg class="abs" style="left:0;top:530px" width="1200" height="150" viewBox="0 0 1200 150">
    <defs><linearGradient id="bandA" x1="0" x2="1"><stop offset="0" stop-color="#2b2fe0"/><stop offset=".5" stop-color="#7a1ea8"/><stop offset="1" stop-color="#e8132a"/></linearGradient></defs>
    <polygon points="0,150 0,22 510,22 630,135 1200,135 1200,150" fill="#060609"/>
    <polyline points="0,20 510,20 632,134 1200,134" fill="none" stroke="url(#bandA)" stroke-width="9"/>
  </svg>
</section>

<section class="about">
  <div class="about-shot abs" role="img" aria-label="Editing software timeline showing coastal footage"></div>
  <div class="about-desk abs" role="img" aria-label="Hands on a color grading control panel"></div>
  <div class="about-text abs">
    <h2 class="heading" style="font-size:42px">ABOUT US</h2>
    <span class="rule"></span>
    <p class="lead">Lanternfold Post is a full-service post-production solution founded by veteran post-production professional Milo Varek.continues through network delivery, and culminates with the completed vision of every partner. We are committed and invested in your success!</p>
    <p class="sub">With over fifteen years of post-production experience, Milo Varek has worked hard to take frustration out of the creative process. During this time, he refined his techniques and brings that expertise to Lanternfold Post, where we offer a consultative, personalized, turn-key solution to each of our unique clients.</p>
  </div>
  <span class="btn about-btn abs">READ MORE</span>
</section>

<section class="services">
  <h2 class="heading heading-center services-head abs" style="font-size:42px">OUR SERVICES<span class="rule"></span></h2>
  <p class="services-intro abs">Lanternfold Post offers color grading, visual effects, audio mixing, offline editorial rentals, edit suite rentals, remote editorial options,&nbsp; conform, and final delivery.</p>
  <div class="service svc-1 abs" role="img" aria-label="Editing software panels"><h3>OFFLINE EDITORIAL</h3></div>
  <div class="service svc-2 abs" role="img" aria-label="Color grading suite">
    <svg class="svc-icon" width="56" height="56" viewBox="0 0 56 56" fill="none" stroke="#fff" stroke-width="2.5"><circle cx="28" cy="28" r="20"/><circle cx="28" cy="28" r="8"/><path d="M28 8v12M28 36v12M8 28h12M36 28h12"/></svg>
    <h3>COLOR GRADING</h3>
    <p>4K HDR Vision Color Grading &amp; Mastering</p>
  </div>
  <div class="service svc-3 abs" role="img" aria-label="Audio mixing console faders"><h3>AUDIO MIXING</h3></div>
  <div class="service svc-4 abs" role="img" aria-label="Close-up of a blue eye"><h3>VISUAL EFFECTS</h3></div>
  <div class="arrow-btn svc-prev abs"><svg width="14" height="14" viewBox="0 0 14 14"><path d="M9 2 4 7l5 5" stroke="#111" stroke-width="2.5" fill="none"/></svg></div>
  <div class="arrow-btn svc-next abs"><svg width="14" height="14" viewBox="0 0 14 14"><path d="M5 2l5 5-5 5" stroke="#111" stroke-width="2.5" fill="none"/></svg></div>
</section>

<section class="videos">
  <h2 class="heading heading-center videos-head abs" style="font-size:42px">OUR VIDEOS<span class="rule"></span></h2>
  <div class="video-side video-left abs" role="img" aria-label="Previous video preview"></div>
  <div class="video-side video-right abs" role="img" aria-label="Next video preview"></div>
  <div class="video-main abs" role="img" aria-label="Video still of a colorist at grading monitors">
    <div class="play abs"><svg width="34" height="38" viewBox="0 0 34 38"><path d="M4 2l28 17L4 36z" fill="#fff"/></svg></div>
    <div class="click-play abs">Click To Play</div>
    <div class="player-bar abs">
      <div class="pb-btn"><svg width="12" height="14" viewBox="0 0 12 14"><path d="M1 1l10 6-10 6z" fill="#fff"/></svg></div>
      <div class="pb-track"><span class="pb-time">01:58</span></div>
    </div>
  </div>
  <div class="video-dots abs"><span></span><span class="on"></span><span></span><span></span><span></span></div>
</section>

<section class="projects abs" style="position:absolute"></section>
<svg class="abs" style="left:0;top:2525px" width="1200" height="140" viewBox="0 0 1200 140">
  <defs><linearGradient id="bandB" x1="0" x2="1"><stop offset="0" stop-color="#e8132a"/><stop offset=".5" stop-color="#7a1ea8"/><stop offset="1" stop-color="#2b2fe0"/></linearGradient></defs>
  <polyline points="0,12 548,12 680,126 1200,126" fill="none" stroke="url(#bandB)" stroke-width="9"/>
</svg>
<h2 class="heading projects-head abs" style="font-size:42px">OUR PROJECTS<span class="rule rule-left"></span></h2>
<div class="poster poster-1 abs" role="img" aria-label="Poster for a reality series with a cast lineup"></div>
<div class="poster poster-2 abs" role="img" aria-label="Poster for a live comedy special"></div>
<div class="poster poster-3 abs" role="img" aria-label="Poster for a family drama series"></div>
<div class="poster-label abs" style="left:147px">PROJECT 01</div>
<div class="poster-label abs" style="left:458px">PROJECT 02</div>
<div class="poster-label abs" style="left:768px">PROJECT 03</div>
<svg class="proj-arrow abs" style="left:72px" width="22" height="30" viewBox="0 0 22 30"><path d="M17 3 5 15l12 12" stroke="#fff" stroke-width="3.5" fill="none"/></svg>
<svg class="proj-arrow abs" style="left:1106px" width="22" height="30" viewBox="0 0 22 30"><path d="M5 3l12 12L5 27" stroke="#fff" stroke-width="3.5" fill="none"/></svg>

<section class="news">
  <h2 class="heading heading-center news-head abs" style="font-size:42px">NEWS &amp; PRESS<span class="rule"></span></h2>
  <article class="news-card abs" style="left:132px;top:3409px">
    <div class="news-logo">Brightcore</div>
    <div class="news-body"><h4>How Creatives Collaborated To Finish Northgate's ....</h4><p>Known for its beautiful imagery and glamor, "Coastal Listings" recently</p><a>READ MORE ›</a></div>
  </article>
  <article class="news-card dark abs" style="left:606px;top:3409px">
    <div class="news-logo">Frameline</div>
    <div class="news-body"><h4>Workflow: Northgate's Coastal Listings</h4><p>Milo Varek is the founder of post company Lanternfold Post</p><a>READ MORE ›</a></div>
  </article>
  <article class="news-card abs" style="left:132px;top:3599px">
    <div class="news-logo">Indie Takes</div>
    <div class="news-body"><h4>Interview with Milo Varek Founder of Lanternfold ....</h4><p>Introducing Milo Varek, founder of post-production company</p><a>READ MORE ›</a></div>
  </article>
  <article class="news-card dark abs" style="left:606px;top:3599px">
    <div class="news-logo yellow">Longform</div>
    <div class="news-body"><h4>Milo Varek of Lanternfold Post On The 5 Things ...</h4><p>It's definitely easy to burn out in this industry. It's important to take</p><a>READ MORE ›</a></div>
  </article>
</section>

<section class="clients">
  <h2 class="heading heading-center clients-head abs" style="font-size:42px">CLIENTS &amp; PARTNERSHIPS<span class="rule"></span></h2>
  <div class="client faded abs" style="left:-42px">Veridia</div>
  <div class="client abs" style="left:143px">Echo Rebels</div>
  <div class="client abs" style="left:328px">Skyline TV</div>
  <div class="client abs" style="left:514px">Searchly</div>
  <div class="client abs" style="left:697px">Cutwell</div>
  <div class="client abs" style="left:882px;font-size:20px">Wren Animation</div>
  <div class="client faded abs" style="left:1067px">Foxglen</div>
</section>

<footer>
  <svg class="abs" style="left:0;top:4122px" width="1200" height="132" viewBox="0 0 1200 132">
    <defs><linearGradient id="bandC" x1="0" x2="1"><stop offset="0" stop-color="#2b2fe0"/><stop offset=".5" stop-color="#7a1ea8"/><stop offset="1" stop-color="#e8132a"/></linearGradient></defs>
    <polygon points="0,132 0,120 522,120 648,10 1200,10 1200,132" fill="#0c0c12"/>
    <polyline points="0,120 522,120 648,10 1200,10" fill="none" stroke="url(#bandC)" stroke-width="9"/>
  </svg>
  <div class="abs" style="left:0;top:4254px;width:1200px;height:423px;background:#0c0c12"></div>
  <div class="foot-col quick abs">
    <h5>QUICK LINKS</h5>
    <ul><li>Home</li><li>About</li><li>Services</li><li>Contact</li><li>Clients</li><li>News</li></ul>
  </div>
  <div class="foot-col contact abs">
    <h5>CONTACT US</h5>
    <ul>
      <li><span class="c-ico"><svg width="10" height="10" viewBox="0 0 10 10"><path d="M2 1l2 2-1 1.5a6 6 0 0 0 2.5 2.5L7 6l2 2-1.5 1.5C4 9 1 6 .5 2.5z" fill="#fff"/></svg></span>+1 310 555 0142</li>
      <li><span class="c-ico"><svg width="10" height="8" viewBox="0 0 10 8"><rect x=".5" y=".5" width="9" height="7" fill="#fff"/><path d="M.5.5 5 4.5 9.5.5" stroke="#2b2fe0" fill="none"/></svg></span>milo@lanternfold.example</li>
      <li><span class="c-ico"><svg width="8" height="11" viewBox="0 0 8 11"><path d="M4 0a4 4 0 0 1 4 4c0 3-4 7-4 7S0 7 0 4a4 4 0 0 1 4-4z" fill="#fff"/><circle cx="4" cy="4" r="1.5" fill="#2b2fe0"/></svg></span>880 Larkmoor Place Hollywood, CA 90028</li>
    </ul>
  </div>
  <div class="foot-col quote abs">
    <h5>REQUEST A QUOTE</h5>
    <span class="field">Name</span>
    <span class="field">Email</span>
    <span class="field">Phone</span>
    <span class="field msg">Message</span>
    <span class="submit">SUBMIT NOW</span>
  </div>
  <p class="copyright abs">© 2024 Lanternfold Post, Inc. | All Rights Reserved</p>
</footer>

</body>
</html>
```